Website for Excavator and Earthworks Company

We require a modern, sleek and practical website for our newly created earthworks/excavator business in Perth, Western Australia called Gullwind Stonecut Earthworks.

The website should have a modern, cutting edge feel but only needs to be relatively simplistic in it's layout and eventual functionality.

Some pages it should have would be Home, About, Projects and Contact Us.

Number of Pages Required

1 page

```html
<!DOCTYPE html>
<html lang="en">
<head>
<meta charset="utf-8">
<title>Gullwind Stonecut Earthworks</title>
<link rel="stylesheet" href="https://fonts.googleapis.com/css2?family=Roboto:wght@400;500;700;900&display=swap">
<style>
:root{
  --lime:#cbdb00;
  --lime-deep:#b9c800;
  --black:#000;
  --bar:#0d0d0d;
  --white:#fff;
  --ink:#1a1a1a;
  --grey:#8a8a8a;
}
*{margin:0;padding:0;box-sizing:border-box}
html,body{width:1200px;height:3934px;overflow:hidden}
body{background:var(--black);color:var(--white);font-family:"Roboto",Arial,sans-serif;position:relative}
.abs{position:absolute}
.btn{position:absolute;background:var(--lime);color:var(--black);font-weight:700;font-size:13px;display:flex;align-items:center;justify-content:center;text-transform:uppercase;letter-spacing:.2px}
.btn.dark{background:var(--black);color:var(--lime)}
.social{display:flex;gap:6px}
.social span{width:34px;height:34px;border-radius:50%;display:block}
.social.filled span:first-child{background:var(--lime)}
.social span{border:2px solid var(--lime)}
.section-title{position:absolute;left:0;width:1200px;text-align:center;font-weight:700;font-size:40px;text-transform:uppercase;letter-spacing:-.3px}
.title-rule{position:absolute;left:556px;width:88px;height:4px;background:var(--lime)}
.wordmark{position:absolute;display:flex;align-items:center;gap:10px;font-weight:900;color:var(--white);text-transform:uppercase;line-height:1.05}
.wordmark i{display:block;width:22px;height:22px;background:var(--lime);flex:none}

/* header */
.site-header{position:absolute;left:0;top:0;width:1200px;height:133px;background:var(--black)}
.site-header .wordmark{left:144px;top:34px;font-size:22px;width:240px}
.site-header .social{position:absolute;left:682px;top:22px}
.call{position:absolute;left:898px;top:20px;display:flex;align-items:center;gap:14px}
.call .ring{width:34px;height:34px;border-radius:50%;background:#1d1d1d;display:flex;align-items:center;justify-content:center}
.call small{display:block;font-size:10px;font-weight:700}
.call b{display:block;font-size:20px;font-weight:700}
.main-nav{position:absolute;top:88px;left:533px;font-size:13px;font-weight:700;text-transform:uppercase}
.main-nav a{position:absolute;color:var(--white);text-decoration:none;white-space:nowrap}
.main-nav a.active{color:var(--lime);text-decoration:underline}

/* hero */
.hero{position:absolute;left:0;top:133px;width:1200px;height:745px}
.hero-photo{position:absolute;left:0;top:0;width:1200px;height:707px;clip-path:polygon(0 0,100% 0,100% 539px,50% 707px,0 539px);
  background:linear-gradient(100deg,#3b3a35 0%,#6d7a73 25%,#a89b86 45%,#b7a58a 60%,#8b7b63 80%,#5c5345 100%)}
.hero-band{position:absolute;left:0;top:0}
.hero-kicker{position:absolute;left:144px;top:144px;font-size:19px;font-weight:500;text-transform:uppercase}
.hero-bar{position:absolute;left:144px;top:187px;width:6px;height:123px;background:var(--lime)}
.hero-title{position:absolute;left:175px;top:182px;font-size:37px;font-weight:700;line-height:44px;text-transform:uppercase}
.hero-sub{position:absolute;left:144px;top:329px;width:400px;font-size:19px;line-height:27px}
.hero .btn{left:144px;top:400px;width:123px;height:40px}
.counter{position:absolute;left:60px;top:230px;writing-mode:vertical-rl;transform:rotate(180deg);font-size:14px;font-weight:700;letter-spacing:2px}
.counter em{color:var(--lime);font-style:normal}
.dots{position:absolute;display:flex;gap:8px}
.dots span{width:13px;height:13px;border-radius:50%;border:2px solid var(--white)}
.dots span.on{background:var(--white)}

/* services */
.card{position:absolute;width:328px;height:302px}
.card-label{position:absolute;width:328px;text-align:center;font-size:20px;font-weight:700;text-transform:uppercase;line-height:30px}
.card-label.hl{color:var(--lime);text-decoration:underline}

/* about */
.about{position:absolute;left:0;top:1582px;width:1200px;height:698px;background:var(--lime)}
.about .wordmark{left:144px;top:130px;font-size:52px;color:var(--black);width:470px;line-height:1.02}
.about-title{position:absolute;left:683px;top:80px;font-size:40px;font-weight:700;color:var(--black);text-transform:uppercase}
.about-copy{position:absolute;left:683px;top:160px;width:374px;color:var(--ink);font-size:14.5px;line-height:24px;text-align:justify}
.about-copy p+p{margin-top:10px}
.about .btn{left:683px;top:458px;width:131px;height:39px}
.about .call{left:836px;top:458px}
.about .call .ring{background:transparent;border:none}
.about .call small,.about .call b{color:var(--black)}
.frame{position:absolute;border:8px solid var(--black)}

/* contact */
.contact{position:absolute;left:0;top:3154px;width:1200px;height:450px;background:linear-gradient(90deg,#bfcd00,#c6d500 50%,#b3c000)}
.contact .section-title{color:var(--black);top:56px}
.field{position:absolute;background:var(--white);border-radius:24px;display:flex;align-items:center;color:#555;font-size:14px}
.field .ic{width:50px;height:100%;display:flex;align-items:center;justify-content:center;border-right:1px solid #ddd;margin-right:12px}
.field.msg{align-items:flex-start;padding-top:14px}
.field.msg .ic{height:auto;padding:2px 0}
.contact .btn{left:522px;top:341px;width:154px;height:42px;background:var(--black);color:var(--lime)}

/* footer */
.site-footer{position:absolute;left:0;top:3604px;width:1200px;height:274px;background:var(--black)}
.site-footer .wordmark{left:144px;top:130px;font-size:24px;width:250px}
.f-head{position:absolute;font-size:16px;font-weight:700;text-transform:uppercase}
.f-rule{position:absolute;width:36px;height:3px;background:var(--lime)}
.f-link{position:absolute;font-size:14px}
.f-ic{position:absolute;width:22px;height:22px;border-radius:50%;background:#222;display:flex;align-items:center;justify-content:center}
.f-text{position:absolute;font-size:13px;line-height:22px}
.subscribe{position:absolute;left:884px;top:134px;width:235px;height:34px;background:var(--white);border-radius:17px;display:flex;align-items:center;padding-left:14px;font-size:10px;color:#555}
.subscribe .go{position:absolute;right:0;top:0;width:44px;height:34px;border-radius:17px;background:var(--lime);display:flex;align-items:center;justify-content:center}
.bottom-bar{position:absolute;left:0;top:3878px;width:1200px;height:56px;background:var(--bar)}
.bottom-bar p{position:absolute;left:0;width:1200px;top:20px;text-align:center;font-size:13px}
.bottom-bar .social{position:absolute;left:968px;top:11px}
</style>
</head>
<body>

<header class="site-header">
  <div class="wordmark"><i></i>Gullwind Stonecut Earthworks</div>
  <div class="social filled"><span></span><span></span><span></span><span></span></div>
  <div class="call">
    <div class="ring"><svg width="16" height="16" viewBox="0 0 24 24"><path fill="#cbdb00" d="M6.6 10.8a15 15 0 0 0 6.6 6.6l2.2-2.2c.3-.3.7-.4 1-.2 1.1.4 2.3.6 3.6.6.6 0 1 .4 1 1V20c0 .6-.4 1-1 1C10.6 21 3 13.4 3 4c0-.6.4-1 1-1h3.5c.6 0 1 .4 1 1 0 1.2.2 2.4.6 3.6.1.3 0 .7-.2 1z"/></svg></div>
    <div><small>CALL US 24/7</small><b>123 456 7890</b></div>
  </div>
  <nav class="main-nav">
    <a class="active" style="left:0">Home</a>
    <a style="left:76px">About</a>
    <a style="left:159px">Projects</a>
    <a style="left:267px">Contact Us</a>
  </nav>
  <div class="btn" style="left:925px;top:76px;width:130px;height:39px">Get a Quote</div>
</header>

<section class="hero">
  <div class="hero-photo" role="img" aria-label="Site worker in hard hat and hi-vis vest overlooking an excavator on a dirt road"></div>
  <svg class="hero-band" width="1200" height="745" viewBox="0 0 1200 745"><polygon fill="#cbdb00" points="0,554 600,722 1200,554 1200,572 600,742 0,572"/></svg>
  <div class="counter">&#8249;&nbsp; <em>02</em> / 03 &nbsp;&#8250;</div>
  <div class="hero-kicker">Gullwind Stonecut Earthworks</div>
  <div class="hero-bar"></div>
  <h1 class="hero-title">Reliable<br>Earthworks<br>Proven Results</h1>
  <p class="hero-sub">Precision work. Modern equipment. Built from the ground up.</p>
  <div class="btn">Contact Us</div>
  <div class="dots" style="left:574px;top:647px"><span></span><span class="on"></span><span></span></div>
</section>

<h2 class="section-title" style="top:953px">Our Earthworks Services</h2>
<div class="title-rule" style="top:1006px"></div>
<div class="card" role="img" aria-label="Bulldozer levelling a graded site" style="left:80px;top:1023px;clip-path:polygon(0 0,100% 24%,100% 100%,0 100%);background:linear-gradient(160deg,#7fb2e0 0%,#b9d3ea 35%,#c79a55 60%,#8a6a45 100%)"></div>
<div class="card" role="img" aria-label="Trench with cables and excavator on roadside" style="left:437px;top:1023px;clip-path:polygon(0 10%,50% 28%,100% 10%,100% 100%,0 100%);background:linear-gradient(160deg,#9a9a8a 0%,#b08a5e 40%,#8a5f3a 70%,#5d4028 100%)"></div>
<div class="card" role="img" aria-label="Concrete drainage pipes lined along a road with workers" style="left:793px;top:1023px;clip-path:polygon(0 24%,100% 0,100% 100%,0 100%);background:linear-gradient(160deg,#bfcfd8 0%,#9aa7a8 35%,#c9c4b8 60%,#8f8578 100%)"></div>
<div class="card-label" style="left:80px;top:1359px">Excavation &amp; Site<br>Preparation</div>
<div class="card-label" style="left:437px;top:1359px">Trenching</div>
<div class="card-label hl" style="left:793px;top:1359px">Drainage &amp; Earthmoving<br>Support</div>
<div class="btn" style="left:519px;top:1455px;width:162px;height:38px">View All Services</div>

<section class="about">
  <div class="wordmark">Gullwind Stonecut Earthworks</div>
  <h2 class="about-title">About Us</h2>
  <div class="about-copy">
    <p>Gullwind Stonecut Earthworks is a Perth-based earthworks and excavation business delivering efficient, high-quality groundwork solutions for residential and commercial projects. As a newly established company, we bring a fresh, modern approach backed by practical experience, attention to detail, and a commitment to getting the job done right.</p>
    <p>Lorem ipsum dolor sit amet, consectetur adipiscing elit, sed do eiusmod tempor incididunt ut labore et dolore magna aliqua. Ut enim ad minim veniam, quis nostrud exercitation ullamco laborisea.</p>
  </div>
  <div class="btn dark">Learn More</div>
  <div class="call">
    <div class="ring"><svg width="20" height="20" viewBox="0 0 24 24"><path fill="#000" d="M6.6 10.8a15 15 0 0 0 6.6 6.6l2.2-2.2c.3-.3.7-.4 1-.2 1.1.4 2.3.6 3.6.6.6 0 1 .4 1 1V20c0 .6-.4 1-1 1C10.6 21 3 13.4 3 4c0-.6.4-1 1-1h3.5c.6 0 1 .4 1 1 0 1.2.2 2.4.6 3.6.1.3 0 .7-.2 1z"/></svg></div>
    <div><small>CALL US 24/7</small><b>123 456 7890</b></div>
  </div>
</section>
<div class="frame" role="img" aria-label="Excavator viewed through the opening of a large concrete pipe" style="left:144px;top:2020px;width:447px;height:336px;background:linear-gradient(135deg,#8c8c88 0%,#c9c9c4 25%,#8ab7e0 45%,#c9a06a 75%,#8a5c35 100%)"></div>
<div class="frame" role="img" aria-label="Orange excavator digging at sunset on a rocky site" style="left:495px;top:2132px;width:560px;height:336px;background:linear-gradient(160deg,#e9b97a 0%,#f3d7a8 25%,#c96d3a 55%,#6b4a32 80%,#3a2c22 100%)"></div>

<h2 class="section-title" style="top:2581px">Recent Projects</h2>
<div class="title-rule" style="top:2632px"></div>
<div class="card" role="img" aria-label="Workers beside an excavator on a dirt site" style="left:-110px;top:2672px;clip-path:polygon(0 10%,100% 0,100% 100%,0 100%);background:linear-gradient(160deg,#d8cbb3 0%,#c2a277 45%,#8f6a45 100%)"></div>
<div class="card" role="img" aria-label="Excavator loading a truck beside a house" style="left:252px;top:2672px;clip-path:polygon(0 0,100% 24%,100% 100%,0 100%);background:linear-gradient(160deg,#8fb9e0 0%,#c8cfd2 35%,#a89d8a 65%,#6b5e50 100%)"></div>
<div class="card" role="img" aria-label="Excavator digging a trench near houses" style="left:614px;top:2672px;clip-path:polygon(0 24%,100% 0,100% 100%,0 100%);background:linear-gradient(160deg,#c9c3b6 0%,#b69970 40%,#8a6442 75%,#5a4030 100%)"></div>
<div class="card" role="img" aria-label="Site worker with an excavator in the background" style="left:976px;top:2672px;clip-path:polygon(0 0,100% 10%,100% 100%,0 100%);background:linear-gradient(160deg,#e0d2bb 0%,#cfae7c 45%,#94714b 100%)"></div>
<div class="card-label" style="left:-110px;top:2993px">Lorem Ipsum Dol</div>
<div class="card-label" style="left:252px;top:2993px">Lorem Ipsum Dol</div>
<div class="card-label hl" style="left:614px;top:2993px">Lorem Ipsum Dol</div>
<div class="card-label" style="left:976px;top:2993px;text-align:left;padding-left:66px">Lorem Ipsum Dol</div>
<div class="dots" style="left:554px;top:3062px"><span></span><span class="on"></span><span></span><span></span><span></span></div>

<section class="contact" role="img" aria-label="Faint lime-toned photo of an excavator on a work site">
  <h2 class="section-title">Contact Us</h2>
  <div class="title-rule" style="top:102px;background:var(--black)"></div>
  <div class="field" style="left:209px;top:149px;width:382px;height:45px"><span class="ic"><svg width="13" height="13" viewBox="0 0 24 24"><circle cx="12" cy="7" r="5" fill="#222"/><path fill="#222" d="M2 23c0-6 4.5-9 10-9s10 3 10 9z"/></svg></span>Your Name</div>
  <div class="field" style="left:209px;top:210px;width:382px;height:45px"><span class="ic"><svg width="13" height="13" viewBox="0 0 24 24"><path fill="#222" d="M6.6 10.8a15 15 0 0 0 6.6 6.6l2.2-2.2c.3-.3.7-.4 1-.2 1.1.4 2.3.6 3.6.6.6 0 1 .4 1 1V20c0 .6-.4 1-1 1C10.6 21 3 13.4 3 4c0-.6.4-1 1-1h3.5c.6 0 1 .4 1 1 0 1.2.2 2.4.6 3.6.1.3 0 .7-.2 1z"/></svg></span>Email</div>
  <div class="field" style="left:209px;top:271px;width:382px;height:45px"><span class="ic"><svg width="14" height="12" viewBox="0 0 24 20"><rect x="1" y="2" width="22" height="16" fill="#222"/><path d="M1 3l11 8 11-8" stroke="#fff" stroke-width="2" fill="none"/></svg></span>Phone</div>
  <div class="field msg" style="left:606px;top:149px;width:385px;height:167px"><span class="ic"><svg width="15" height="13" viewBox="0 0 24 20"><ellipse cx="10" cy="8" rx="9" ry="6.5" fill="#222"/><path fill="#222" d="M4 12l-2 6 6-3z"/></svg></span>Your Message</div>
  <div class="btn">Send Message</div>
</section>

<footer class="site-footer">
  <div class="wordmark"><i></i>Gullwind Stonecut Earthworks</div>
  <div class="f-head" style="left:453px;top:80px">Company</div>
  <div class="f-rule" style="left:453px;top:108px"></div>
  <div class="f-link" style="left:453px;top:131px">Home</div>
  <div class="f-link" style="left:453px;top:163px">About</div>
  <div class="f-link" style="left:453px;top:195px">Projects</div>
  <div class="f-link" style="left:453px;top:226px">Contact Us</div>

  <div class="f-head" style="left:597px;top:80px">Contact Us</div>
  <div class="f-rule" style="left:597px;top:108px"></div>
  <div class="f-ic" style="left:595px;top:135px"><svg width="10" height="10" viewBox="0 0 24 24"><path fill="#cbdb00" d="M6.6 10.8a15 15 0 0 0 6.6 6.6l2.2-2.2c.3-.3.7-.4 1-.2 1.1.4 2.3.6 3.6.6.6 0 1 .4 1 1V20c0 .6-.4 1-1 1C10.6 21 3 13.4 3 4c0-.6.4-1 1-1h3.5c.6 0 1 .4 1 1 0 1.2.2 2.4.6 3.6.1.3 0 .7-.2 1z"/></svg></div>
  <div class="f-text" style="left:635px;top:135px">123 456 7890</div>
  <div class="f-ic" style="left:595px;top:175px"><svg width="10" height="9" viewBox="0 0 24 20"><rect x="1" y="2" width="22" height="16" fill="#cbdb00"/><path d="M1 3l11 8 11-8" stroke="#222" stroke-width="2" fill="none"/></svg></div>
  <div class="f-text" style="left:635px;top:175px">info@gullwindstonecut.com</div>
  <div class="f-ic" style="left:595px;top:215px"><svg width="9" height="11" viewBox="0 0 20 26"><path fill="#cbdb00" d="M10 0a9 9 0 0 0-9 9c0 7 9 17 9 17s9-10 9-17a9 9 0 0 0-9-9z"/><circle cx="10" cy="9" r="3.5" fill="#222"/></svg></div>
  <div class="f-text" style="left:635px;top:215px;width:240px">465, Gullwind Stonecut Earthworks, Perth Western Australia</div>

  <div class="f-head" style="left:884px;top:80px">Subscribe</div>
  <div class="f-rule" style="left:884px;top:108px"></div>
  <div class="subscribe">&#9993;&nbsp; Email Address<span class="go"><svg width="14" height="14" viewBox="0 0 24 24"><path fill="#000" d="M2 11L22 2l-7 20-3-8z"/></svg></span></div>
</footer>
<div class="bottom-bar">
  <p>Copyright© 2026 &nbsp;/&nbsp; All Rights Reserved</p>
  <div class="social filled"><span></span><span></span><span></span><span></span></div>
</div>

</body>
</html>
```